www.brightlingua.example -- International Language school needs a Wordpress Design

NOTE: This is for a complete WordPress website with coding (Design/develop)

We are a small, private English language school in business for 15 years. Our students come from around the world to study English at our centre in Toronto, Canada. Most of our students are in their 20's and come to study English with us for periods of 1-6 months before returning home to complete their post-secondary education or pursue their careers.

We are looking for a talented web designer to redevelop our sadly outdated website (www.brightlingua.example) to bring a fresh look with vastly increased functionality and web traffic.

Target Market(s)

-20s and 30s; mostly upper-middle class, educated
-from non-English speaking countries, but often have some English background
-looking to improve their English (mostly speaking) skills at our school like ours and experience living in a new country (like exchange students)

Industry/Entity Type

Education

Font styles to use
Sans Serif

Requirements
Must have
• - page listing our programs
- page with our fees and starting dates
- application form
- page showing why BRIGHT (us)?
- page with accommodation options
* responsive design
Nice to have
• examples of other websites in our industry I like:

http://www.maryholt.example/
http://www.tqlearn.example/en
http://en.rpz.example/
http://www.harrowgate-college.example/

```html
<!DOCTYPE html>
<html lang="en">
<head>
<meta charset="utf-8">
<title>BRIGHT International English Language Centre</title>
<link href="https://fonts.googleapis.com/css2?family=Raleway:wght@400;500;600&family=Open+Sans:wght@400;600&display=swap" rel="stylesheet">
<style>
:root{
  --green:#8cc63f;
  --green-dark:#6fa52a;
  --blue:#2a87c8;
  --blue-dark:#1f6fa8;
  --orange:#f7a21b;
  --ink:#222;
  --muted:#666;
  --line:#d8d8d8;
  --band:#f3f3f3;
}
*{box-sizing:border-box;margin:0;padding:0}
html,body{width:801px;height:1200px;overflow:hidden;background:#fff}
body{position:relative;font-family:"Open Sans",sans-serif;color:var(--ink)}
.abs{position:absolute}

/* header */
.brand{left:101px;top:8px;display:flex;align-items:flex-end;gap:10px}
.brand-mark{width:22px;height:22px;border-radius:50%;background:var(--blue);margin-bottom:40px}
.brand-name{font-family:"Raleway",sans-serif;font-weight:600;font-size:28px;color:var(--ink);line-height:1;position:absolute;left:0;top:50px}
.brand-title{left:185px;top:64px;font-family:"Raleway",sans-serif;font-weight:600;font-size:10.5px}
.lang{left:641px;top:25px;width:60px;height:17px;border:1px solid var(--line);font-size:7px;display:flex;align-items:center;gap:4px;padding-left:5px}
.lang i{width:11px;height:7px;background:#2a4b8d;display:block}
.city{left:542px;top:68px;font-size:6.5px;letter-spacing:.3px}
.social{left:651px;top:64px;display:flex;gap:4px}
.social span{width:13px;height:13px;background:var(--blue-dark);border-radius:2px}

/* nav */
.nav{left:0;top:86px;width:801px;height:28px;background:linear-gradient(#9ed34f,var(--green-dark));display:flex;justify-content:center}
.nav a{font-family:"Raleway",sans-serif;font-size:9.2px;color:#fff;text-decoration:none;padding:0 11px;line-height:28px;border-right:1px solid rgba(255,255,255,.35)}
.nav a:last-child{border-right:0}

/* hero */
.hero{left:0;top:114px;width:801px;height:281px;background:linear-gradient(90deg,#8b8680,#c9c2b8 45%,#6e8fb4 65%,#9a958d)}
.hero-tag{left:100px;top:225px;width:232px;height:64px;background:rgba(42,135,200,.9);clip-path:polygon(0 0,100% 0,93% 100%,0 100%);color:#fff;font-family:"Raleway",sans-serif;padding:10px 0 0 22px}
.hero-tag b{display:block;font-weight:400;font-size:20px;line-height:22px}
.hero-tag span{font-size:13px}
.dots{left:380px;top:376px;display:flex;gap:3px}
.dots i{width:9px;height:9px;border-radius:50%;background:#fff}
.dots i:first-child{background:#111}

/* actions */
.action{top:410px;width:180px;text-align:center}
.action .ico{width:50px;height:50px;border-radius:50%;background:var(--blue);margin:0 auto 4px;display:flex;align-items:center;justify-content:center}
.action h3{font-family:"Raleway",sans-serif;font-weight:400;font-size:14px;color:var(--blue)}
.action p{font-size:7.5px;color:#444;margin-top:1px}
.rule{left:101px;top:507px;width:599px;height:1px;background:var(--line)}

/* intro */
.intro{left:120px;top:531px;width:561px;text-align:center}
.intro h2{font-family:"Raleway",sans-serif;font-weight:400;font-size:18px;margin-bottom:6px}
.intro p{font-size:7px;line-height:12px;color:#444}

/* programs */
.tile{width:198px;height:140px}
.tile .photo{height:98px}
.tile .cap{height:42px;color:#fff;text-align:center;font-family:"Raleway",sans-serif;padding-top:7px}
.tile .cap h4{font-weight:500;font-size:12px;line-height:13px}
.tile .cap p{font-size:7px;opacity:.85;margin-top:2px}
.blue{background:var(--blue)} .orange{background:var(--orange)} .green{background:var(--green)}

/* sidebar */
.box{left:539px;width:161px;border:1px solid var(--line)}
.box h5{font-family:"Raleway",sans-serif;font-weight:500;font-size:11.5px;text-align:center;background:linear-gradient(#fff,#eee);border-bottom:1px solid var(--line);height:27px;line-height:27px}
.feed{display:flex;gap:6px;padding:8px 10px 0 13px;height:48px}
.feed .av{width:28px;height:26px;background:#b08a74;flex:none}
.feed b{font-weight:400;font-size:6.5px;display:block}
.feed p{font-size:5.5px;color:#888;line-height:8px}
.feed em{font-style:normal;font-size:5.5px;display:block;margin-top:2px}
.life{text-align:center;font-size:8px;padding-top:11px}
.life p{margin-bottom:9px}

/* band */
.band{left:0;top:947px;width:801px;height:175px;background:var(--band);border-top:1px solid #eaeaea;border-bottom:1px solid #eaeaea}
.card{top:969px;width:142px;height:129px;background:#fff;border:1px solid #e2e2e2}
.card .photo{height:75px}
.card h4{font-family:"Raleway",sans-serif;font-weight:500;font-size:10.5px;color:var(--green-dark);margin:7px 0 2px 10px}
.card p{font-size:6.3px;color:#888;margin-left:10px;line-height:10px}

/* footer */
.flinks{left:101px;top:1148px;font-size:7px}
.copy{left:101px;top:1165px;font-size:6.5px}
.badges{left:442px;top:1145px;display:flex;gap:14px;align-items:center}
.badges i{display:block;background:#9db3cc}
</style>
</head>
<body>
<header>
  <div class="abs brand"><span class="brand-mark"></span></div>
  <div class="abs brand-name" style="left:101px;top:56px;font-family:'Raleway',sans-serif;font-weight:600;font-size:24px">bright</div>
  <div class="abs brand-title">BRIGHT International English Language Centre</div>
  <div class="abs lang"><i></i>English ▾</div>
  <div class="abs city">TORONTO * CANADA</div>
  <div class="abs social"><span></span><span></span><span></span></div>
</header>

<nav class="abs nav">
  <a>HOME</a><a>OUR SCHOOL</a><a>PROGRAMS</a><a>FEES &amp; DATES</a><a>ACCOMMODATION</a><a>AFTER CLASS</a><a>AGENTS</a><a>CONTACT</a>
</nav>

<section class="abs hero" role="img" aria-label="Photo of two smiling students in a classroom"></section>
<div class="abs hero-tag"><b>PRIVATE ENGLISH</b><span>Language Learning school</span></div>
<div class="abs dots"><i></i><i></i><i></i><i></i></div>

<div class="abs action" style="left:147px">
  <div class="ico"><svg width="26" height="26" viewBox="0 0 26 26"><circle cx="13" cy="13" r="11" fill="#fff"/><text x="13" y="18" text-anchor="middle" font-family="Open Sans,sans-serif" font-weight="600" font-size="14" fill="#2a87c8">?</text></svg></div>
  <h3>Ask a Question</h3><p>Lorem ipsum dolor sit amet consect</p>
</div>
<div class="abs action" style="left:331px;top:408px">
  <div class="ico"><svg width="28" height="24" viewBox="0 0 28 24"><ellipse cx="11" cy="9" rx="9" ry="7" fill="none" stroke="#fff" stroke-width="2"/><ellipse cx="18" cy="14" rx="8" ry="6" fill="none" stroke="#fff" stroke-width="2"/></svg></div>
  <h3>Get a Quote</h3><p>Lorem ipsum dolor sit amet consect</p>
</div>
<div class="abs action" style="left:516px;top:408px">
  <div class="ico"><svg width="26" height="26" viewBox="0 0 26 26"><circle cx="13" cy="13" r="11" fill="#fff"/><path d="M8 13l4 4 7-8" fill="none" stroke="#2a87c8" stroke-width="3"/></svg></div>
  <h3>Apply Now</h3><p>Lorem ipsum dolor sit amet consect</p>
</div>
<div class="abs rule"></div>

<section class="abs intro">
  <h2>BRIEF INTRO TO SCHOOL</h2>
  <p>cligula augue bibendum accumsan vestibulum ut commodo a mi Morbi ornare gravida elit Integer congue augue et malesuada iaculis ipsum dui aliquet felis at cursus magna nisl nec elit Praesent elementum elit at tellus nec ultricies sit amet porttitor mattis enim In massa libero interdum nec interdum vel blandit sed nulla In ullamcorper est eget tempor cursus neque mi consectetuer mi a ultricies massa est sed nisl Class apte</p>
</section>

<article class="abs tile" style="left:101px;top:625px"><div class="photo" style="background:linear-gradient(#c9b89a,#8a7a64)" role="img" aria-label="Adult students around a classroom table"></div><div class="cap blue"><h4>Adult English Programs</h4><p>Curabitur iaculis tempus eros Curabitur vel</p></div></article>
<article class="abs tile" style="left:314px;top:625px"><div class="photo" style="background:linear-gradient(#6f7b6a,#3c4238)" role="img" aria-label="Young students studying together"></div><div class="cap orange"><h4>Junior Camps Parent<br>&amp; Child Program</h4></div></article>
<article class="abs tile" style="left:101px;top:779px"><div class="photo" style="background:linear-gradient(#4d6fa4,#2c4a82)" role="img" aria-label="Students in rain ponchos on a trip"></div><div class="cap green"><h4>Pathway Program</h4><p>Curabitur iaculis tempus eros Curabitur vel</p></div></article>
<article class="abs tile" style="left:314px;top:779px"><div class="photo" style="background:linear-gradient(#5f7fa0,#3f5a7c)" role="img" aria-label="Students in life jackets on a boating trip"></div><div class="cap blue"><h4>Working Holiday Programs</h4><p>Curabitur iaculis tempus eros Curabitur vel</p></div></article>

<aside class="abs box" style="top:624px;height:177px">
  <h5>Community Feed</h5>
  <div class="feed"><div class="av" role="img" aria-label="Member avatar"></div><div><b>Etiam eu urna</b><p>Malesuada nec ultricies sit amet portti-tor mattis enim In massa libe</p><em>Posted 2 hours ago</em></div></div>
  <div class="feed"><div class="av" role="img" aria-label="Member avatar"></div><div><b>Nulla sit amet diam</b><p>Malesuada nec ultricies sit amet port-titmattis enim In massa liber</p><em>Posted 2 hours ago</em></div></div>
  <div class="feed"><div class="av" role="img" aria-label="Member avatar"></div><div><b>Donec convallis pede</b><p>Malesuada nec ultricies sit amet portti-tor mattis enim In massa libero</p><em>Posted 2 hours ago</em></div></div>
</aside>
<aside class="abs box" style="top:809px;height:108px">
  <h5 style="font-size:12px">STUDENT LIFE</h5>
  <div class="life"><p>Meet our Students</p><p>Videos</p><p>Photos</p></div>
</aside>

<div class="abs band"></div>
<article class="abs card" style="left:100px"><div class="photo" style="background:linear-gradient(#8a8c92,#5c5a55)" role="img" aria-label="Aerial view of the Toronto skyline"></div><h4>About Toronto</h4><p>Lorem ipsum dolor sit amet consect etuer adipiscing elit Nam</p></article>
<article class="abs card" style="left:253px"><div class="photo" style="background:linear-gradient(#c8c2b4,#7f786c)" role="img" aria-label="Students studying downtown"></div><h4>Downtown Location</h4><p>Lorem ipsum dolor sit amet consect etuer adipiscing elit Nam</p></article>
<article class="abs card" style="left:406px"><div class="photo" style="background:linear-gradient(#7a7875,#504a46)" role="img" aria-label="Students in a school lounge"></div><h4>Daily Workshops</h4><p>Lorem ipsum dolor sit amet consect etuer adipiscing elit Nam</p></article>
<article class="abs card" style="left:559px"><div class="photo" style="background:linear-gradient(#9a6a52,#5c4538)" role="img" aria-label="Students doing a group activity"></div><h4>Free Friday Activities</h4><p>Lorem ipsum dolor sit amet consect etuer adipiscing elit Nam</p></article>

<footer>
  <div class="abs flinks">Home | Our School | Programs | Fees &amp; Dates | Accommodation | After Class | Agents | Contact</div>
  <div class="abs copy">© 2015 Company Name All right reserved Term of Use</div>
  <div class="abs badges">
    <i style="width:44px;height:20px"></i>
    <i style="width:55px;height:20px"></i>
    <i style="width:36px;height:20px"></i>
    <i style="width:22px;height:22px;border-radius:50%"></i>
    <i style="width:52px;height:20px"></i>
  </div>
</footer>
</body>
</html>
```